Velira....Soft Light, Deep Calm

I would like a hologram or golden seed of life as my logo or something along those lines with my business name Velira and then underneath....Soft Light, Deep Calm. Maybe black background....I’m not sure.
On the back, a list of my offerings,
*Lantern of Stillness /Learning to Breathe
*Connection to Source/Self
*Life Changing/Developing
*Plant Medicine consultation
*Conscious Awareness
Velira_lumo@morvexmail.com
Kelmar: 0437215096
I want my card to look inviting, caring and loving....but with a deep dive into human consciousness 👁💫.
Show me what you got🙏🏽

Designs look the same

```html
<!DOCTYPE html>
<html lang="en">
<head>
<meta charset="utf-8">
<title>Velira — Business Cards</title>
<link rel="stylesheet" href="https://fonts.googleapis.com/css2?family=Alegreya+Sans:wght@400;500&display=swap">
<style>
  :root {
    --stage: #2b2b2d;
    --card: #050505;
    --sky: #3ab7e6;
    --lime: #c8dd34;
    --white: #f2f2f2;
    --rule: #9a9a9a;
    --font: "Alegreya Sans", sans-serif;
  }
  * { margin: 0; padding: 0; box-sizing: border-box; }
  html, body {
    width: 1200px; height: 1108px; overflow: hidden;
    background: var(--stage);
    font-family: var(--font);
  }
  .canvas { position: relative; width: 1200px; height: 1108px; }
  .card {
    position: absolute; top: 174px;
    width: 440px; height: 760px;
    background: var(--card);
    border-radius: 24px;
    overflow: hidden;
    box-shadow: 0 18px 40px rgba(0,0,0,.5);
  }
  .card--offerings { left: 120px; }
  .card--identity {
    left: 640px;
    background: radial-gradient(ellipse at 50% 45%, #141414, var(--card) 70%);
  }

  /* offerings side */
  .pattern-field {
    position: absolute; left: 0; top: 0; width: 440px; height: 470px;
    background:
      radial-gradient(ellipse at 50% 30%, rgba(58,183,230,.55), rgba(58,183,230,0) 60%),
      radial-gradient(ellipse at 55% 75%, rgba(200,221,52,.45), rgba(200,221,52,0) 55%),
      var(--card);
  }
  .offerings {
    position: absolute; left: 40px; right: 40px; top: 500px;
    list-style: none; text-align: center;
  }
  .offerings li {
    font-size: 23px; line-height: 1;
    padding: 10px 0;
    border-bottom: 1px solid var(--rule);
  }
  .offerings li:last-child { border-bottom: none; }
  .tone-lime { color: var(--lime); }
  .tone-sky { color: var(--sky); }
  .tone-white { color: var(--white); }

  /* identity side */
  .mark-circle {
    position: absolute; left: 85px; top: 110px;
    width: 270px; height: 270px;
    border: 2px solid var(--sky); border-radius: 50%;
  }
  .brand {
    position: absolute; left: 0; right: 0; top: 400px; text-align: center;
  }
  .brand__name {
    color: var(--sky); font-size: 64px; font-weight: 400; letter-spacing: 2px; line-height: 1;
  }
  .brand__tagline {
    color: var(--lime); font-size: 26px; letter-spacing: 1px; margin-top: 6px;
  }
  .brand__dash {
    width: 20px; height: 3px; background: var(--sky); margin: 34px auto 0;
  }
  .contact {
    position: absolute; left: 0; right: 0; top: 568px; text-align: center;
    font-size: 23px; line-height: 1.6; color: var(--white);
  }
  .contact__label { color: var(--sky); }
</style>
</head>
<body>
<main class="canvas">
  <section class="card card--offerings">
    <div class="pattern-field" role="img" aria-label="Glowing sacred geometry pattern of overlapping circles in blue, lime and white"></div>
    <ul class="offerings">
      <li><span class="tone-lime">Lantern of Stillness</span> <span class="tone-white">/Learning to Breathe</span></li>
      <li class="tone-lime">Connection to Source/Self</li>
      <li class="tone-sky">Life Changing/Developing</li>
      <li class="tone-sky">Plant Medicine consultation</li>
      <li class="tone-sky">Conscious Awareness</li>
    </ul>
  </section>

  <section class="card card--identity">
    <div class="mark-circle"></div>
    <div class="brand">
      <h1 class="brand__name">VELIRA</h1>
      <p class="brand__tagline">SOFT LIGHT, DEEP CALM</p>
      <div class="brand__dash"></div>
    </div>
    <div class="contact">
      <p><span class="contact__label">Kelmar:</span> 0437215096</p>
      <p>Velira_lumo@morvexmail.com</p>
    </div>
  </section>
</main>
</body>
</html>
```